1 pager agency advertisement flyer

We need a fresh logo and advertising flyer for my insurance company based in Richmond VA. We have recently signed an agreement with a sizable company to become their preferred insurance provider. We specialize in Several things but focusing on Auto, Home, Renters, Roadside assistance, Landlord, Motorcycles, Boats, and Condos. We also offer a full portfolio of financial services. I would like to see options with Blue, yellow and white, and also black(I know), Yellow, and white. The name of the agency is Talvor Insurance Services Inc. Discounts are key in what we do: Discounts to advertise: Multi policy, 19% early signing, safe driver rewards, and EASY PAYMENT OPTIONS. A phrase like: "as an employee you are eligible for a 19% signing discount" SIDE NOTE: The people that we have already written business for the average saving currently stands at 28% annually.

Industry/Entity Type

Graphic Design

```html
<!DOCTYPE html>
<html lang="en">
<head>
<meta charset="utf-8">
<title>Talvor Insurance Services Inc. – Flyer</title>
<link rel="stylesheet" href="https://fonts.googleapis.com/css2?family=Archivo+Black&family=Anton&family=Roboto:wght@700;900&display=swap">
<style>
  :root {
    --blue: #2f55e0;
    --blue-deep: #1b33b8;
    --green: #8cc63f;
    --ink: #0d0d0d;
    --white: #ffffff;
    --gold: #d9b77c;
    --gold-dark: #6b4722;
    --badge-green: #7be04a;
    --badge-red: #e3141a;
  }
  * { margin: 0; padding: 0; box-sizing: border-box; }
  html, body { width: 846px; height: 1200px; overflow: hidden; background: var(--white); }
  .flyer { position: relative; width: 846px; height: 1200px; overflow: hidden; background: var(--white); font-family: "Roboto", Arial, sans-serif; }
  .backdrop { position: absolute; inset: 0; }
  .brand {
    position: absolute; left: 14px; top: 10px; width: 118px; height: 118px;
    display: flex; flex-direction: column; align-items: center; justify-content: center; gap: 8px;
    background: var(--white); border: 4px solid var(--blue);
    font-weight: 900; font-size: 13px; line-height: 1.15;
    color: var(--blue-deep); text-align: center;
  }
  .brand-dot { width: 22px; height: 22px; background: var(--blue-deep); }
  .company-name {
    position: absolute; left: 160px; right: 110px; top: 14px; text-align: center;
    font-family: "Archivo Black", Arial, sans-serif; font-size: 47px; line-height: 57px;
    color: var(--blue); -webkit-text-stroke: 2px var(--ink); letter-spacing: 1px;
  }
  .headline {
    position: absolute; left: 0; right: 0; top: 470px; text-align: center;
    font-family: "Anton", Impact, sans-serif; font-size: 62px; line-height: 70px;
    color: var(--blue); -webkit-text-stroke: 1.5px var(--blue-deep);
    text-shadow: 3px 3px 2px rgba(0,0,0,.75); letter-spacing: 1.5px;
  }
  .coverage-grid {
    position: absolute; left: 150px; top: 634px; width: 548px;
    display: grid; grid-template-columns: repeat(4, 130px); gap: 10px 9px;
  }
  .coverage-tile {
    height: 128px; background: var(--white); border: 6px solid var(--ink);
    display: flex; flex-direction: column; align-items: center; justify-content: space-between;
    padding: 8px 2px 6px;
  }
  .coverage-tile svg { width: 80px; height: 74px; }
  .coverage-label { font-weight: 900; font-size: 21px; color: var(--ink); line-height: 1; text-align: center; }
  .coverage-label.small { font-size: 13px; line-height: 1.05; }
  .coverage-label.mid { font-size: 15px; }
  .coverage-label.landlord { font-size: 17px; }
  .discount-row { position: absolute; left: 0; right: 0; top: 916px; height: 170px; }
  .seal { position: absolute; width: 210px; height: 170px; }
  .seal svg { position: absolute; inset: 0; }
  .seal-text {
    position: absolute; left: 30px; right: 30px; top: 0; bottom: 0;
    display: flex; align-items: center; justify-content: center;
  }
  .seal-copy {
    display: block; text-align: center;
    font-family: "Anton", Impact, sans-serif; font-size: 19px; line-height: 22px;
    color: var(--badge-green); -webkit-text-stroke: 1px #1c3a10; text-transform: uppercase;
  }
  .seal-copy .accent, .seal-copy.alert { color: var(--badge-red); -webkit-text-stroke: 1px #4a0406; }
  .seal-copy .accent { font-size: 22px; }
  .savings-note {
    position: absolute; left: 0; right: 0; top: 1142px; text-align: center;
    font-weight: 900; font-size: 12.5px; color: var(--blue-deep);
  }
</style>
</head>
<body>
<main class="flyer">
  <svg class="backdrop" width="846" height="1200" viewBox="0 0 846 1200">
    <defs>
      <linearGradient id="photoTone" x1="0" y1="0" x2="1" y2="0">
        <stop offset="0" stop-color="#d9e8e4"/>
        <stop offset="0.12" stop-color="#f1e4da"/>
        <stop offset="0.3" stop-color="#e6cdbd"/>
        <stop offset="0.45" stop-color="#eef0f2"/>
        <stop offset="0.6" stop-color="#b9dbea"/>
        <stop offset="0.75" stop-color="#9fc9dc"/>
        <stop offset="0.88" stop-color="#c9b49c"/>
        <stop offset="1" stop-color="#eef1f3"/>
      </linearGradient>
      <linearGradient id="photoShade" x1="0" y1="0" x2="0" y2="1">
        <stop offset="0" stop-color="#ffffff" stop-opacity="0.35"/>
        <stop offset="0.45" stop-color="#ffffff" stop-opacity="0"/>
        <stop offset="1" stop-color="#f4f6f8" stop-opacity="0.85"/>
      </linearGradient>
    </defs>
    <g role="img" aria-label="Photo of smiling medical staff in white coats and surgical masks giving a thumbs up">
      <path d="M0 0 H846 V90 C 760 330 640 560 420 700 C 300 770 150 790 0 800 Z" fill="url(#photoTone)"/>
      <path d="M0 0 H846 V90 C 760 330 640 560 420 700 C 300 770 150 790 0 800 Z" fill="url(#photoShade)"/>
    </g>
    <path d="M846 90 C 760 330 640 560 420 700 C 300 770 150 790 0 800 L0 830 C 170 820 330 800 460 730 C 660 610 790 420 846 230 Z" fill="var(--green)"/>
    <path d="M846 230 C 790 420 660 610 460 730 C 330 800 170 820 0 830 L0 880 C 120 860 260 840 400 780 C 600 690 760 520 846 300 Z" fill="var(--white)"/>
    <path d="M846 300 C 760 520 600 690 400 780 C 260 840 120 860 0 880 L0 1098 L846 1098 Z" fill="var(--blue)"/>
    <path d="M846 360 C 790 560 680 700 560 780 L600 790 C 720 700 810 560 846 420 Z" fill="var(--white)"/>
    <path d="M846 440 C 800 620 720 740 610 800 L846 800 Z" fill="var(--green)" opacity="0.9"/>
    <path d="M846 520 C 810 660 750 760 660 820 L846 820 Z" fill="var(--blue)"/>
    <rect x="0" y="1098" width="846" height="102" fill="var(--green)"/>
  </svg>

  <div class="brand"><span class="brand-dot"></span>Talvor Insurance Services</div>

  <h1 class="company-name">TALVOR INSURANCE<br>SERVICE INC</h1>

  <h2 class="headline">YOUR BEST&nbsp; ALL RISKS BUSINESS<br>INSURACE DOCTOR</h2>

  <section class="coverage-grid">
    <div class="coverage-tile">
      <svg viewBox="0 0 80 74"><path d="M4 50 L8 40 L22 37 L33 28 H54 L66 36 L77 39 V50 Z" fill="#000"/><circle cx="20" cy="51" r="7" fill="#000" stroke="#fff" stroke-width="2"/><circle cx="62" cy="51" r="7" fill="#000" stroke="#fff" stroke-width="2"/><path d="M36 31 H46 V36 H30 Z M50 31 H54 L62 36 H50 Z" fill="#fff"/></svg>
      <span class="coverage-label">AUTO</span>
    </div>
    <div class="coverage-tile">
      <svg viewBox="0 0 80 74"><path d="M40 6 L74 36 H64 V68 H48 V48 H32 V68 H16 V36 H6 Z" fill="#000"/><rect x="56" y="10" width="8" height="16" fill="#000"/></svg>
      <span class="coverage-label">HOME</span>
    </div>
    <div class="coverage-tile">
      <svg viewBox="0 0 80 74"><circle cx="22" cy="20" r="16" fill="#000"/><circle cx="22" cy="20" r="6" fill="#fff"/><path d="M32 30 L70 66 L62 72 L56 66 L60 62 L54 56 L50 60 L28 36 Z" fill="#000"/></svg>
      <span class="coverage-label">RENTERS</span>
    </div>
    <div class="coverage-tile">
      <svg viewBox="0 0 80 74">
        <circle cx="40" cy="15" r="13" fill="none" stroke="#000" stroke-width="3"/>
        <text x="39" y="20" text-anchor="middle" font-family="Roboto, Arial, sans-serif" font-weight="900" font-size="13">24</text>
        <text x="53" y="8" font-family="Roboto, Arial, sans-serif" font-weight="900" font-size="6">HR</text>
        <g stroke="#000" stroke-linecap="round">
          <line x1="20" y1="38" x2="62" y2="70" stroke-width="7"/>
          <line x1="60" y1="38" x2="18" y2="70" stroke-width="7"/>
        </g>
        <path d="M10 30 A10 10 0 1 0 26 44 L20 40 L18 34 Z" fill="#000"/>
        <path d="M70 30 A10 10 0 1 1 54 44 L60 40 L62 34 Z" fill="#000"/>
        <rect x="13" y="64" width="10" height="8" rx="2" fill="#000" transform="rotate(-37 18 68)"/>
        <rect x="57" y="64" width="10" height="8" rx="2" fill="#000" transform="rotate(37 62 68)"/>
      </svg>
      <span class="coverage-label small">ROADSIDE<br>ASSISTANCE</span>
    </div>
    <div class="coverage-tile">
      <svg viewBox="0 0 80 74"><circle cx="16" cy="54" r="12" fill="none" stroke="#000" stroke-width="4"/><circle cx="64" cy="54" r="12" fill="none" stroke="#000" stroke-width="4"/><path d="M16 54 L32 40 H50 L64 54 M44 40 L40 26" stroke="#000" stroke-width="5" fill="none"/><circle cx="40" cy="12" r="8" fill="#000"/><path d="M36 20 L44 22 L48 38 H36 Z" fill="#000"/></svg>
      <span class="coverage-label mid">MOTORCYCLE</span>
    </div>
    <div class="coverage-tile">
      <svg viewBox="0 0 80 74"><path d="M2 46 L20 30 L38 46 V70 H2 Z M24 40 L44 14 L64 40 V70 H24 Z M42 46 L60 30 L78 46 V70 H42 Z" fill="#000" stroke="#fff" stroke-width="2"/></svg>
      <span class="coverage-label landlord">Landlord</span>
    </div>
    <div class="coverage-tile">
      <svg viewBox="0 0 80 74"><path d="M38 4 V54 H10 Z" fill="#000"/><path d="M42 10 C 60 24 66 40 66 54 H42 Z" fill="#000"/><path d="M6 58 H74 L64 70 H16 Z" fill="#000"/></svg>
      <span class="coverage-label">BOATS</span>
    </div>
    <div class="coverage-tile">
      <svg viewBox="0 0 80 74"><rect x="26" y="8" width="28" height="62" fill="#000"/><rect x="8" y="30" width="18" height="40" fill="#000"/><rect x="54" y="24" width="18" height="46" fill="#000"/><g fill="#fff"><rect x="31" y="14" width="6" height="6"/><rect x="43" y="14" width="6" height="6"/><rect x="31" y="26" width="6" height="6"/><rect x="43" y="26" width="6" height="6"/><rect x="31" y="38" width="6" height="6"/><rect x="43" y="38" width="6" height="6"/><rect x="31" y="50" width="6" height="6"/><rect x="43" y="50" width="6" height="6"/></g></svg>
      <span class="coverage-label">CONDO</span>
    </div>
  </section>

  <section class="discount-row">
    <div class="seal" style="left:9px">
      <svg viewBox="0 0 210 170"><path d="M0 62 H40 V108 H0 L14 85 Z M210 62 H170 V108 H210 L196 85 Z" fill="var(--gold-dark)"/><circle cx="105" cy="85" r="78" fill="var(--gold-dark)"/><circle cx="105" cy="85" r="70" fill="var(--gold)" stroke="#f3dcae" stroke-width="3"/><rect x="20" y="66" width="170" height="38" fill="var(--gold)" stroke="var(--gold-dark)" stroke-width="3"/></svg>
      <div class="seal-text"><span class="seal-copy">GET<br>MULTI POLICY<br>DISCOUNT</span></div>
    </div>
    <div class="seal" style="left:213px">
      <svg viewBox="0 0 210 170"><path d="M0 62 H40 V108 H0 L14 85 Z M210 62 H170 V108 H210 L196 85 Z" fill="var(--gold-dark)"/><circle cx="105" cy="85" r="78" fill="var(--gold-dark)"/><circle cx="105" cy="85" r="70" fill="var(--gold)" stroke="#f3dcae" stroke-width="3"/><rect x="20" y="66" width="170" height="38" fill="var(--gold)" stroke="var(--gold-dark)" stroke-width="3"/></svg>
      <div class="seal-text"><span class="seal-copy">GET<br><span class="accent">19%</span> EARLY<br>SIGNING</span></div>
    </div>
    <div class="seal" style="left:423px">
      <svg viewBox="0 0 210 170"><path d="M0 62 H40 V108 H0 L14 85 Z M210 62 H170 V108 H210 L196 85 Z" fill="var(--gold-dark)"/><circle cx="105" cy="85" r="78" fill="var(--gold-dark)"/><circle cx="105" cy="85" r="70" fill="var(--gold)" stroke="#f3dcae" stroke-width="3"/><rect x="20" y="66" width="170" height="38" fill="var(--gold)" stroke="var(--gold-dark)" stroke-width="3"/></svg>
      <div class="seal-text"><span class="seal-copy">GET<br>SAFE DRIVER<br>REWARD</span></div>
    </div>
    <div class="seal" style="left:627px">
      <svg viewBox="0 0 210 170"><path d="M0 62 H40 V108 H0 L14 85 Z M210 62 H170 V108 H210 L196 85 Z" fill="var(--gold-dark)"/><circle cx="105" cy="85" r="78" fill="var(--gold-dark)"/><circle cx="105" cy="85" r="70" fill="var(--gold)" stroke="#f3dcae" stroke-width="3"/><rect x="20" y="66" width="170" height="38" fill="var(--gold)" stroke="var(--gold-dark)" stroke-width="3"/></svg>
      <div class="seal-text"><span class="seal-copy alert">EASY<br>PAYMENT<br>OPTIONS</span></div>
    </div>
  </section>

  <p class="savings-note">The people that we have already written business for the average saving currently stands at 28% annually.</p>
</main>
</body>
</html>
```